Security Camera Sign

14” high x 11” wide Color: Blue, Yellow, Black and white

Make the sign vertical
Replace red with blue
WARNING: Black over yellow
These premises are protected by Closed Circuit Television: On white
Images are recorded for crime prevention and public safety. Unauthorized access, theft or vandalism will result in prosecution: On Blue

Target Market(s)

Outdoor commercial building

Industry/Entity Type

Security

Requirements
Nice to have
• I would like the sign stand out. If you need more colors? Thanks Ok

```html
<!DOCTYPE html>
<html lang="en">
<head>
<meta charset="UTF-8">
<title>Security Camera Warning Sign</title>
<link href="https://fonts.googleapis.com/css2?family=Source+Sans+3:wght@700;800&display=swap" rel="stylesheet">
<style>
  :root {
    --backdrop: #dfe3e6;
    --sign-blue: #141a85;
    --sign-yellow: #e9ef00;
    --ink: #0b0b0b;
    --face-white: #eef3f6;
    --rim-white: #ffffff;
    --screw: #b9c0c6;
    --camera-tone-a: #f4f6f8;
    --camera-tone-b: #c9cdd2;
  }
  html, body {
    margin: 0;
    padding: 0;
    width: 1200px;
    height: 804px;
    overflow: hidden;
    background: var(--backdrop);
    font-family: "Source Sans 3", "Myriad Pro", sans-serif;
  }
  .canvas {
    position: relative;
    width: 1200px;
    height: 804px;
  }
  .sign {
    position: absolute;
    left: 301px;
    top: 22px;
    width: 598px;
    height: 760px;
    background: var(--rim-white);
    border-radius: 40px;
    padding: 6px;
    box-sizing: border-box;
    box-shadow: 0 6px 18px rgba(0,0,0,0.25);
  }
  .sign-panel {
    position: relative;
    width: 100%;
    height: 100%;
    box-sizing: border-box;
    border: 3px solid var(--ink);
    border-radius: 34px;
    overflow: hidden;
    background: var(--sign-blue);
  }
  .screw {
    position: absolute;
    top: 52px;
    width: 20px;
    height: 20px;
    border-radius: 50%;
    background: radial-gradient(circle at 40% 35%, #ffffff, var(--screw) 60%, #7d858c);
    border: 1px solid #6b7279;
  }
  .screw--left { left: 22px; }
  .screw--right { right: 22px; }
  .headline-bar {
    position: absolute;
    left: 60px;
    top: 20px;
    width: 460px;
    height: 88px;
    background: var(--sign-yellow);
    border: 3px solid var(--ink);
    border-radius: 8px;
    box-sizing: border-box;
    display: flex;
    align-items: center;
    justify-content: center;
  }
  .headline {
    margin: 0;
    font-weight: 800;
    font-size: 78px;
    line-height: 1;
    letter-spacing: 1px;
    color: var(--ink);
    transform: translateY(-2px);
  }
  .notice-field {
    position: absolute;
    left: 0;
    top: 128px;
    width: 100%;
    height: 434px;
    background: var(--face-white);
  }
  .notice-text {
    position: absolute;
    left: 0;
    top: 18px;
    width: 100%;
    margin: 0;
    text-align center;
    text-align: center;
    font-weight: 700;
    font-size: 42px;
    line-height: 46px;
    color: var(--ink);
    letter-spacing: -0.3px;
  }
  .camera-illustration {
    position: absolute;
    left: 110px;
    top: 172px;
    width: 360px;
    height: 246px;
    background: linear-gradient(160deg, var(--camera-tone-a), var(--camera-tone-b));
    border-radius: 8px;
  }
  .legal-band {
    position: absolute;
    left: 0;
    top: 562px;
    width: 100%;
    height: 180px;
    display: flex;
    align-items: center;
    justify-content: center;
  }
  .legal-text {
    margin: 0;
    width: 540px;
    text-align: center;
    color: var(--rim-white);
    font-weight: 700;
    font-size: 25px;
    line-height: 31px;
  }
</style>
</head>
<body>
<div class="canvas">
  <div class="sign">
    <div class="sign-panel">
      <span class="screw screw--left"></span>
      <span class="screw screw--right"></span>
      <div class="headline-bar">
        <h1 class="headline">WARNING</h1>
      </div>
      <div class="notice-field">
        <p class="notice-text">THESE PREMISES ARE<br>PROTECTED BY CLOSED<br>CIRCUIT TELEVISION</p>
        <div class="camera-illustration" role="img" aria-label="Line illustration of a wall-mounted security camera"></div>
      </div>
      <div class="legal-band">
        <p class="legal-text">IMAGES ARE RECORDED FOR CRIME<br>PREVENTION AND PUBLIC SAFETY.<br>UNAUTHORIZED ACCESS, THEFT OR<br>VANDALISM WILL RESULT IN<br>PROSECUTION</p>
      </div>
    </div>
  </div>
</div>
</body>
</html>
```